Health Care Service Company Flyer

Company name: Bright Harbor Clinic
Slogan: Find out what you're made of
Website: brightharborclinic.ca

I need the flyer to contain the company name (will provide logo source file ASAP), the slogan in large font and a "find out more at harborclinic.ca"

Other important data to include in the flyer is:
Four bullet points with the following information:
*Track performance and fitness results over time
*Develop proprietary exercise and dietary programs based on actionable data
*Track muscle atrophy from injury, as well as muscle gain during rehabilitation
*Reveal imbalances in muscle symmetry and strength, flexibility, and joint mechanics

I also need the following information conveyed somewhere on the flyer:
*Body Fat, Muscle Mass, and Bone Density Measurements
• Over 50 data points generated in each 10 minute scan
*Call XXX-XXX-XXX to book an appointment today

DEXA Body Composition Services.
Get scanned today.

See example of competitor flyers in the images to get an example of the images and information we are trying to convey

Target Market(s)

athletes, fitness enthusiast, crossfit

Industry/Entity Type

Health And Wellness

Colors
33a6d7
acd036

Requirements
Nice to have
• Prefer images be general health and wellness related - in other words, individuals who look healthy, but are not abnormally muscular
Should not have
• Shirtless models, No big muscles,

```html
<!DOCTYPE html>
<html lang="en">
<head>
<meta charset="utf-8">
<title>Bright Harbor Clinic – Flyer</title>
<link rel="stylesheet" href="https://fonts.googleapis.com/css2?family=Anton&family=Jost:wght@400;600;700&family=Roboto+Condensed:wght@400&display=swap">
<style>
  :root {
    --ink: #111111;
    --night: #0e0e0e;
    --sky: #5fd6f2;
    --sky-bright: #22d7f3;
    --sky-deep: #1aa6e2;
    --sky-pale: #8de8f7;
    --lime: #a6ee1a;
    --white: #ffffff;
    --text: #2a2a2a;
  }
  html, body {
    margin: 0;
    width: 1200px;
    height: 1200px;
    overflow: hidden;
    background: var(--white);
  }
  .stage {
    position: absolute;
    left: 0; top: 0;
    width: 1500px; height: 1500px;
    transform: scale(0.8);
    transform-origin: 0 0;
  }
  .flyer {
    position: absolute;
    left: 271px; top: 65px;
    width: 957px; height: 1353px;
    overflow: hidden;
    background: var(--white);
  }
  .flyer-art { position: absolute; inset: 0; }
  .brand {
    position: absolute;
    left: 14px; top: 56px;
    display: flex; align-items: center; gap: 22px;
  }
  .brand-mark {
    width: 30px; height: 30px;
    background: #050505;
  }
  .brand-name {
    font-family: "Jost", sans-serif;
    font-weight: 700;
    font-size: 40px;
    letter-spacing: 2px;
    text-transform: uppercase;
    color: var(--sky-bright);
  }
  .slogan {
    position: absolute;
    left: 130px; top: 210px;
    font-family: "Anton", sans-serif;
    line-height: 1;
    margin: 0;
    font-weight: 400;
  }
  .slogan-lead {
    display: block;
    color: var(--lime);
    font-size: 74px;
    transform: rotate(-9deg);
    transform-origin: left bottom;
    margin-left: 4px;
  }
  .slogan-main {
    display: block;
    color: var(--white);
    font-size: 66px;
    transform: rotate(-11deg);
    transform-origin: left bottom;
    margin-top: 8px;
    margin-left: 14px;
    white-space: nowrap;
  }
  .benefits {
    position: absolute;
    left: 64px; top: 796px;
    margin: 0; padding: 0;
    list-style: none;
    font-family: "Roboto Condensed", sans-serif;
    font-size: 25px;
    color: var(--text);
  }
  .benefits li { height: 41px; line-height: 41px; }
  .benefits li::before { content: "•"; margin-right: 7px; }
  .divider { position: absolute; left: 48px; top: 980px; }
  .scan-title {
    position: absolute; left: 0; right: 0; top: 1018px;
    text-align: center;
    font-family: "Jost", sans-serif; font-weight: 700;
    font-size: 29px; color: var(--lime); margin: 0;
  }
  .scan-detail {
    position: absolute; left: 0; right: 0; top: 1055px;
    text-align: center;
    font-family: "Jost", sans-serif; font-weight: 400;
    font-size: 28px; color: var(--text); margin: 0;
  }
  .booking {
    position: absolute; left: 0; right: 0; top: 1118px;
    text-align: center;
    font-family: "Jost", sans-serif; font-weight: 400;
    font-size: 38px; line-height: 1.2; color: var(--lime); margin: 0;
  }
  .website {
    position: absolute; left: 0; right: 0; top: 1294px;
    text-align: center;
    font-family: "Jost", sans-serif; font-weight: 400;
    font-size: 22px; letter-spacing: 5px; color: var(--white); margin: 0;
  }
</style>
</head>
<body>
<div class="stage">
  <main class="flyer">
    <svg class="flyer-art" viewBox="0 0 957 1353" width="957" height="1353">
      <defs>
        <linearGradient id="runner-top" x1="0" y1="0" x2="1" y2="0">
          <stop offset="0" stop-color="#2a2220"/>
          <stop offset="0.5" stop-color="#c9c6c4"/>
          <stop offset="1" stop-color="#3a2f2c"/>
        </linearGradient>
        <linearGradient id="beach" x1="0" y1="0" x2="0" y2="1">
          <stop offset="0" stop-color="#b9dcef"/>
          <stop offset="0.5" stop-color="#2f5d7d"/>
          <stop offset="0.8" stop-color="#4b7592"/>
          <stop offset="1" stop-color="#c8d8e2"/>
        </linearGradient>
        <radialGradient id="portrait" cx="0.5" cy="0.45" r="0.6">
          <stop offset="0" stop-color="#c9a088"/>
          <stop offset="0.6" stop-color="#7a9aa8"/>
          <stop offset="1" stop-color="#6fb2d8"/>
        </radialGradient>
      </defs>
      <rect class="top-band" x="0" y="0" width="957" height="270" fill="var(--night)"/>
      <polygon role="img" aria-label="Photo of a runner in a white t-shirt" points="600,0 957,0 957,132 640,172" fill="url(#runner-top)"/>
      <polygon class="hero-band" points="0,262 957,132 957,530 0,772" fill="var(--sky)"/>
      <polygon points="0,262 190,535 0,772" fill="var(--sky-bright)"/>
      <polygon points="0,772 190,535 310,560" fill="var(--sky-deep)"/>
      <polygon points="190,535 310,560 640,612 330,520" fill="#3cc3ec"/>
      <polygon points="560,400 957,132 957,175" fill="var(--sky-pale)"/>
      <polygon role="img" aria-label="Photo of a man jogging along a beach" points="560,400 957,160 957,530 640,612" fill="url(#beach)"/>
      <circle cx="456" cy="563" r="182" fill="var(--lime)"/>
      <circle role="img" aria-label="Photo of a smiling woman holding a water bottle outdoors" cx="456" cy="563" r="168" fill="url(#portrait)"/>
      <g class="footer-band">
        <polygon points="0,1196 545,1190 957,1182 957,1353 0,1353" fill="#5fd4f2"/>
        <polygon points="0,1196 660,1285 957,1353 0,1353" fill="#4cc8ee"/>
        <polygon points="0,1353 545,1192 770,1270 660,1353" fill="var(--sky-deep)"/>
        <polygon points="770,1270 957,1182 957,1353 660,1353" fill="#7ad9f3"/>
        <polygon points="770,1270 957,1333 957,1353 660,1353" fill="#1598dc"/>
      </g>
    </svg>

    <div class="brand">
      <span class="brand-mark"></span>
      <span class="brand-name">Bright Harbor Clinic</span>
    </div>

    <h1 class="slogan">
      <span class="slogan-lead">FIND OUT</span>
      <span class="slogan-main">WHAT YOU'RE MADE OF</span>
    </h1>

    <ul class="benefits">
      <li>Track performance and fitness results over time</li>
      <li>Develop proprietary exercise and dietary programs based on actionable data</li>
      <li>Track muscle atrophy from injury, as well as muscle gain during rehabilitation</li>
      <li>Reveal imbalances in muscle symmetry and strength, flexibility, and joint mechanics</li>
    </ul>

    <svg class="divider" width="860" height="16" viewBox="0 0 860 16">
      <line x1="7" y1="8" x2="853" y2="8" stroke="var(--sky-bright)" stroke-width="2"/>
      <circle cx="7" cy="8" r="7" fill="var(--lime)"/>
      <circle cx="430" cy="8" r="7" fill="var(--lime)"/>
      <circle cx="853" cy="8" r="7" fill="var(--lime)"/>
    </svg>

    <h2 class="scan-title">Body Fat, Muscle Mass, and Bone Density Measurements</h2>
    <p class="scan-detail">• Over 50 data points generated in each 10 minute scan</p>
    <p class="booking">Call XXX-XXX-XXX to book an appointment today</p>
    <p class="website">Website: brightharborclinic.ca</p>
  </main>
</div>
</body>
</html>
```